Junior Showdown Flyer for Holiday Program

Need a one page flyer, can be back to front or one page, ensuring you can fit all information, colourful, aimed at a market of 8-13 year old boys and girls.
The flyer needs to be noticed, needs to have certain information on it and needs to be Autralian Rule Football orientated.
Have uploaded file so you can understand the style (not content), style of flyer I am looking at getting submitted.

Target Market(s)

8-13 year old boys and girls and their parents.

Requirements
Must have
• Junior Showdown Event
• Price for Junior Showdown Day will be $85
• Strictly Limited Places, only the best footballers should enter this challenge
• Inaugural event, be the first Junior Showdown Winner for your age!
• Do you love a challenge! Put yourself to the test!
• Are you up to it - Water Slide Goal Kicking Contest! The fastest kick in the West (tested by our very own speed gun)! Can you survive the Football Gladiator Course or Topple Mania Goal Kicking! These challenges are crazy are super fun!
• If you think you can deliver on the big stage then this is for YOU!
• All District age winners will receive prizes, awards and the adulation from all their peers!
• Year's 3-5 from 9am to 12pm
• Year's 6-8 from 1-4pm
• All challengers compete against their own age
• Lunch Provided
• Monday 16th April - Kestrel Bay Junior Showdown Day at Brindle Park
• Tuesday 17th April - Marlow Ridge Junior Showdown Day at Collumbi Reserve
• Wednesday 18th April - Tarrin Junior Showdown Day - Yandell Football Club
• Every Challenge Participant receives a District Football!
• Need to put all 3 District Football Logos on the bottom of the flyer, logos attached at bottom.
Nice to have
• Plenty of colour, if you can fit all information on one page that would be fine
Should not have
• Dull, boring, any footballs should be Aussie Rules footballs not NFL or soccer

```html
<!DOCTYPE html>
<html lang="en">
<head>
<meta charset="utf-8">
<title>Junior Showdown Event</title>
<link href="https://fonts.googleapis.com/css2?family=Kaushan+Script&family=Ubuntu:ital,wght@0,700;1,700&display=swap" rel="stylesheet">
<style>
  :root {
    --navy: #1c2b5c;
    --teal: #12927f;
    --red: #e31e24;
    --ink: #2e2e33;
    --paper: #ffffff;
  }
  * { margin: 0; padding: 0; box-sizing: border-box; }
  html, body { width: 846px; height: 1200px; overflow: hidden; background: var(--paper); }
  .flyer {
    position: relative;
    width: 846px;
    height: 1200px;
    overflow: hidden;
    background: var(--paper);
    font-family: "Ubuntu", Arial, sans-serif;
  }
  .flyer__waves { position: absolute; inset: 0; width: 846px; height: 1200px; z-index: 0; }
  .flyer__title {
    position: absolute;
    z-index: 1;
    top: 88px;
    right: 40px;
    width: 420px;
    text-align: center;
    color: var(--navy);
    font-family: "Kaushan Script", cursive;
    font-size: 74px;
    line-height: 1;
    letter-spacing: 4px;
    text-transform: uppercase;
  }
  .flyer__subtitle {
    position: absolute;
    z-index: 1;
    top: 170px;
    right: 92px;
    color: var(--teal);
    font-style: italic;
    font-weight: 700;
    font-size: 25px;
  }
  .details {
    position: absolute;
    z-index: 1;
    top: 239px;
    left: 38px;
    width: 730px;
    list-style: none;
  }
  .details li {
    position: relative;
    padding-left: 25px;
    color: var(--ink);
    font-weight: 700;
    font-size: 16.2px;
    line-height: 34.8px;
    white-space: nowrap;
  }
  .details li::before {
    content: "";
    position: absolute;
    left: 2px;
    top: 15px;
    width: 6px;
    height: 6px;
    border-radius: 50%;
    background: var(--red);
  }
  .partners {
    position: absolute;
    z-index: 1;
    left: 0;
    top: 1090px;
    width: 846px;
    display: flex;
    justify-content: space-around;
    padding: 0 40px;
  }
  .partner {
    display: flex;
    align-items: center;
    gap: 10px;
    color: var(--navy);
    font-weight: 700;
    font-size: 19px;
  }
  .partner__dot {
    width: 30px;
    height: 30px;
    border-radius: 50%;
    background: var(--teal);
  }
  .partner--terriers .partner__dot { background: var(--red); }
  .partner--tarrin .partner__dot { background: var(--navy); }
  .flyer__footer-band {
    position: absolute;
    left: 0;
    bottom: 0;
    width: 846px;
    height: 18px;
    background: var(--red);
  }
</style>
</head>
<body>
<main class="flyer">
  <svg class="flyer__waves" viewBox="0 0 705 1000" preserveAspectRatio="none" aria-hidden="true">
    <path fill="var(--navy)" d="M0,0 H705 V80 C665,35 610,12 545,8 C420,2 300,58 180,88 C110,106 50,110 0,104 Z"/>
    <path fill="var(--teal)" d="M0,112 C55,118 115,114 185,96 C300,66 430,14 545,16 C430,30 310,86 190,122 C115,144 55,148 0,142 Z"/>
    <path fill="none" stroke="var(--teal)" stroke-width="9" d="M630,40 C700,150 708,400 664,560 C612,742 470,830 255,850"/>
    <path fill="var(--navy)" d="M705,220 C700,500 645,715 485,790 C385,832 255,838 135,808 C72,790 30,765 0,728 V770 C62,818 200,845 335,845 C505,843 640,825 705,790 Z"/>
    <path fill="none" stroke="var(--teal)" stroke-width="7" d="M0,690 C40,780 130,845 262,862"/>
  </svg>

  <h1 class="flyer__title">Junior</h1>
  <p class="flyer__subtitle">Showdown Event</p>

  <ul class="details">
    <li>Price for Junior Showdown Day will be $85</li>
    <li>Strictly Limited Places, only the best footballers should enter this challenge</li>
    <li>Inaugural event, be the first Junior Showdown Winner for your age!</li>
    <li>Do you love a challenge! Put yourself to the test!</li>
    <li>Are you up to it - Water Slide Goal Kicking Contest! The fastest kick in the West<br>(tested by our very own speed gun)! Can you survive the Football Gladiator Course or Topple<br>Mania Goal Kicking! These challenges are crazy are super fun!</li>
    <li>If you think you can deliver on the big stage then this is for YOU!</li>
    <li>All District age winners will receive prizes, awards and the adulation from all their peers!</li>
    <li>Year's 3-5 from 9am to 12pm</li>
    <li>Year's 6-8 from 1-4pm</li>
    <li>All challengers compete against their own age</li>
    <li>Lunch Provided</li>
    <li>Monday 16th April - Kestrel Bay Junior Showdown Day at Brindle Park</li>
    <li>Tuesday 17th April - Marlow Ridge Junior Showdown Day at Collumbi Reserve</li>
    <li>Wednesday 18th April - Tarrin Junior Showdown Day - Yandell Football Club</li>
    <li>Every Challenge Participant receives a District Football!</li>
  </ul>

  <div class="partners">
    <div class="partner partner--stingrays"><span class="partner__dot"></span>Stingrays District</div>
    <div class="partner partner--terriers"><span class="partner__dot"></span>Terriers District</div>
    <div class="partner partner--tarrin"><span class="partner__dot"></span>Tarrin District</div>
  </div>

  <div class="flyer__footer-band"></div>
</main>
</body>
</html>
```